Business Card Design Project

We are an incubator company that helps young entrepreneur to launch new ideas into the market. We will be targeting investors or likewise; Angels, young entrepreneurs and technopreneurs.

Our logo is being tasked by artflockly to design, therefore there is no logo for now.
You can us Lanternfold Pte Ltd as the logo for the time being.

Please let us have some versions of modern and yet professional designs; for words, you can indicate e.g (address), (Title)

thanks

Target Market(s)

young entrepreneurs
angels, investors

Industry/Entity Type

Business

Colors
3176b5
ffffff

Requirements
Must have
• able to project out our name; Lanternfold
Should not have
• Nothing childish or cartoon

```html
<!DOCTYPE html>
<html lang="en">
<head>
<meta charset="utf-8">
<title>Lanternfold Pte Ltd — Business Card</title>
<link rel="stylesheet" href="https://fonts.googleapis.com/css2?family=Open+Sans:wght@400;600;700&display=swap">
<style>
  :root {
    --stage: #1c1d20;
    --card-blue: #2146e6;
    --card-edge: #1834c2;
    --card-glow: #4a8cf5;
    --lime: #8df02a;
    --white: #ffffff;
  }
  * { box-sizing: border-box; margin: 0; padding: 0; }
  html, body {
    width: 1200px;
    height: 900px;
    overflow: hidden;
    background: var(--stage);
    font-family: "Open Sans", sans-serif;
  }
  .canvas {
    position: relative;
    width: 1200px;
    height: 900px;
  }
  .card {
    position: absolute;
    width: 550px;
    height: 310px;
    background: var(--card-blue);
    border: 6px solid var(--card-edge);
    overflow: hidden;
  }
  .card-surface {
    position: absolute;
    inset: 0;
    background:
      radial-gradient(ellipse 70% 60% at 55% 95%, var(--card-glow) 0%, rgba(74,140,245,0) 70%),
      linear-gradient(180deg, #1f40e2 0%, #2a58ee 100%);
  }
  .card-front { left: 40px; top: 150px; }
  .card-back { left: 610px; top: 470px; }

  .wordmark {
    position: absolute;
    left: 30px;
    top: 24px;
    display: flex;
    align-items: center;
    gap: 12px;
  }
  .wordmark-mark {
    width: 34px;
    height: 34px;
    border-radius: 50%;
    background: var(--lime);
  }
  .wordmark-name {
    font-weight: 700;
    font-size: 27px;
    color: var(--lime);
    letter-spacing: 0.2px;
    white-space: nowrap;
  }

  .contact-grid {
    position: absolute;
    left: 30px;
    right: 14px;
    bottom: 18px;
    display: grid;
    grid-template-columns: 190px 150px auto;
    row-gap: 16px;
    color: var(--white);
    font-size: 12.5px;
    font-weight: 600;
  }
  .contact-item {
    display: flex;
    align-items: center;
    gap: 8px;
    white-space: nowrap;
  }
  .contact-item svg { width: 13px; height: 13px; flex: none; }
  .contact-item.small { font-size: 11px; font-weight: 400; }

  .back-wordmark {
    position: absolute;
    left: 0;
    right: 0;
    top: 118px;
    text-align: center;
    font-weight: 700;
    font-size: 28px;
    letter-spacing: 1px;
    color: var(--lime);
    white-space: nowrap;
  }
</style>
</head>
<body>
<main class="canvas">

  <section class="card card-front" aria-label="Business card front">
    <div class="card-surface" role="img" aria-label="Blue background with soft light bokeh circles"></div>

    <div class="wordmark">
      <span class="wordmark-mark" aria-hidden="true"></span>
      <span class="wordmark-name">Lanternfold Pte Ltd</span>
    </div>

    <div class="contact-grid">
      <div class="contact-item">
        <svg viewBox="0 0 12 12" aria-hidden="true"><circle cx="6" cy="3.2" r="2.6" fill="var(--lime)"/><path d="M1 12 C1 7.5 11 7.5 11 12 Z" fill="var(--lime)"/></svg>
        <span>Name and Surname</span>
      </div>
      <div class="contact-item">
        <svg viewBox="0 0 12 12" aria-hidden="true"><path d="M3 1 L5 1 L5.5 3.5 L4 4.5 C4.6 6 6 7.4 7.5 8 L8.5 6.5 L11 7 L11 9 C11 10 10 11 9 11 C5 11 1 7 1 3 C1 2 2 1 3 1 Z" fill="var(--lime)"/></svg>
        <span>Telephone</span>
      </div>
      <div class="contact-item small">
        <svg viewBox="0 0 12 12" aria-hidden="true"><circle cx="6" cy="6" r="5" fill="none" stroke="var(--lime)" stroke-width="1.4"/><path d="M1 6 H11 M6 1 C3.5 4 3.5 8 6 11 M6 1 C8.5 4 8.5 8 6 11" fill="none" stroke="var(--lime)" stroke-width="1"/></svg>
        <span>www.yourwebsite.com</span>
      </div>
      <div class="contact-item">
        <svg viewBox="0 0 12 12" aria-hidden="true"><path d="M6 11.5 C2.5 7.5 2 6 2 4.5 A4 4 0 0 1 10 4.5 C10 6 9.5 7.5 6 11.5 Z" fill="var(--lime)"/><circle cx="6" cy="4.5" r="1.6" fill="var(--card-blue)"/></svg>
        <span>Address</span>
      </div>
      <div class="contact-item">
        <svg viewBox="0 0 12 12" aria-hidden="true"><rect x="3" y="1" width="6" height="4" fill="none" stroke="var(--lime)" stroke-width="1.2"/><rect x="1" y="5" width="10" height="5" rx="1" fill="var(--lime)"/><rect x="3" y="8" width="6" height="3" fill="var(--white)"/></svg>
        <span>Fax</span>
      </div>
      <div class="contact-item small">
        <svg viewBox="0 0 12 12" aria-hidden="true"><rect x="1" y="2.5" width="10" height="7" fill="none" stroke="var(--lime)" stroke-width="1.2"/><path d="M1 2.5 L6 6.5 L11 2.5" fill="none" stroke="var(--lime)" stroke-width="1.2"/></svg>
        <span>your@email.com</span>
      </div>
    </div>
  </section>

  <section class="card card-back" aria-label="Business card back">
    <div class="card-surface" role="img" aria-label="Blue background with soft light bokeh circles"></div>
    <p class="back-wordmark">Lanternfold Pte Ltd</p>
  </section>

</main>
</body>
</html>
```